Letterhead for Midwest Law Firm

Our law firm does estate planning and trust administration in Wisconsin and Illinois. We recently obtained a new logo and need to incorporate it into new stationary. The stationary needs to list out the attorneys at the firm, but we will want 3 variations, one with three attorneys, one with six, and one with six plus the names of states where each is licensed to practice (possibly as an asterisk with notation somewhere towards bottom of page. As with most traditional law practices, letterhead should be conservative and convey predictability and reliability. We view our brand as being primarily reliability, with prestige as a secondary element. We are upmarket, but would like to avoid seeming pretentious or "slick". We are a smaller firm with a personal touch.

Target Market(s)

Affluent Midwestern Americans approaching at or approaching retirement age.

Industry/Entity Type

Legal

Font styles to use
Serif
Sans Serif

Requirements
Must have
• Must use our logo. Must comply with Brennick Legal Guild Ethics rules: https://www.halvorjudic.org/courts/offices/docs/pqmtnv20annotated.pdf. Must be conventional. Must list names of attorneys and provide contact information for firm. Note that we are asking for three designs with very minor variations. Also, designer must provide letterhead in a format that is industry-standard for stationary printers.
Nice to have
• We would appreciate an alternate version that will look reasonable when printed on a black-and-white printer. Designer can use judgment as to whether to have use grayscale, black/white, or something in between.
Should not have
• No "motto" or "visit our website" extraneous materials. putting the website address somewhere is fine, but overall there is a lot of required text, and we'd like to not appear cluttered.

```html
<!DOCTYPE html>
<html lang="en">
<head>
<meta charset="utf-8">
<title>Hollisford &amp; Crane LLP — Letterhead</title>
<link rel="stylesheet" href="https://fonts.googleapis.com/css2?family=Libre+Baskerville:wght@400;700&display=swap">
<style>
  :root {
    --backdrop: #dedede;
    --paper: #fafafa;
    --paper-bright: #ffffff;
    --navy: #2a2a40;
    --ink: #4a4a55;
    --gold: #f0a92a;
    --sky: #1ea3dc;
    --watermark: #f1f0ee;
  }
  * { margin: 0; padding: 0; box-sizing: border-box; }
  html, body {
    width: 1200px; height: 800px; overflow: hidden;
    background: var(--backdrop);
    font-family: "Libre Baskerville", Georgia, serif;
  }
  .canvas { position: relative; width: 1200px; height: 800px; }

  .sheet {
    position: absolute;
    top: 111px;
    width: 410px; height: 574px;
    background: var(--paper);
    color: var(--ink);
  }
  .sheet--full { left: 165px; }
  .sheet--partners { left: 613px; background: var(--paper-bright); }

  .firm-mark { position: absolute; display: flex; align-items: center; gap: 6px; color: var(--navy); }
  .firm-mark__dot { width: 9px; height: 9px; border-radius: 50%; background: var(--gold); flex: none; }
  .firm-mark__name { font-size: 12px; font-weight: 700; white-space: nowrap; }
  .sheet--full .firm-mark { left: 118px; top: 30px; }
  .sheet--partners .firm-mark { left: 34px; top: 64px; }

  .roster { position: absolute; list-style: none; font-size: 6.3px; line-height: 10.2px; text-transform: uppercase; letter-spacing: 0.1px; color: var(--ink); }
  .roster--partners-left { left: 37px; top: 80px; }
  .roster--associates { left: 231px; top: 74px; }
  .roster--partners-right { left: 267px; top: 57px; line-height: 11.2px; }

  .watermark { position: absolute; left: 120px; top: 200px; width: 170px; height: 170px; border-radius: 50%; background: var(--watermark); }

  .contact { position: absolute; bottom: 34px; left: 37px; font-size: 7.4px; line-height: 10.4px; color: var(--ink); }
  .contact__line { display: flex; align-items: center; gap: 3px; }
  .contact__icon { width: 7px; height: 7px; fill: var(--sky); }
  .address { position: absolute; bottom: 34px; right: 36px; font-size: 7.4px; line-height: 10.4px; text-align: right; color: var(--ink); font-style: normal; }
</style>
</head>
<body>
<div class="canvas">

  <section class="sheet sheet--full" aria-label="Letterhead with partners and associates">
    <div class="firm-mark"><span class="firm-mark__dot"></span><span class="firm-mark__name">Hollisford &amp; Crane LLP</span></div>
    <ul class="roster roster--partners-left">
      <li>Walter C. Hollisford</li>
      <li>Dennis J. Crane</li>
      <li>Oliver R. Hollisford</li>
    </ul>
    <ul class="roster roster--associates">
      <li>Anton A. Brezinski, Sr. Associate</li>
      <li>Laura J. Kettering, Sr. Associate</li>
      <li>Joanne A. Prisbeck, Sr. Associate</li>
      <li>Carla A. Wendtland, Associate</li>
    </ul>
    <div class="watermark" role="img" aria-label="Faint firm emblem"></div>
    <div class="contact">
      <div class="contact__line"><svg class="contact__icon" viewBox="0 0 10 10"><path d="M1 3.5C1 2 2.5 1 5 1s4 1 4 2.5L7.3 4 7 3H3l-.3 1zM2.5 5h5l1 4h-7z"/></svg>414-555-0148</div>
      <div class="contact__line"><svg class="contact__icon" viewBox="0 0 10 10"><path d="M3 1h4v2H3zM1 4h8v4H7.5v1.5h-5V8H1zM3 7h4v2H3z"/></svg>414-555-0172</div>
    </div>
    <address class="address">218 E. Larkfield Avenue,<br>Suite 300&nbsp; Milwaukee, WI&nbsp; 53204</address>
  </section>

  <section class="sheet sheet--partners" aria-label="Letterhead with partners only">
    <div class="firm-mark"><span class="firm-mark__dot"></span><span class="firm-mark__name">Hollisford &amp; Crane LLP</span></div>
    <ul class="roster roster--partners-right">
      <li>Walter C. Hollisford</li>
      <li>Dennis J. Crane</li>
      <li>Oliver R. Hollisford</li>
    </ul>
    <div class="watermark" role="img" aria-label="Faint firm emblem"></div>
    <div class="contact">
      <div class="contact__line"><svg class="contact__icon" viewBox="0 0 10 10"><path d="M1 3.5C1 2 2.5 1 5 1s4 1 4 2.5L7.3 4 7 3H3l-.3 1zM2.5 5h5l1 4h-7z"/></svg>414-555-0148</div>
      <div class="contact__line"><svg class="contact__icon" viewBox="0 0 10 10"><path d="M3 1h4v2H3zM1 4h8v4H7.5v1.5h-5V8H1zM3 7h4v2H3z"/></svg>414-555-0172</div>
    </div>
    <address class="address">218 E. Larkfield Avenue,<br>Suite 300&nbsp; Milwaukee, WI&nbsp; 53204</address>
  </section>

</div>
</body>
</html>
```